Business Card Design Project

Im an electrician and my company name is Kestrel Electrical
My main work is installing Lighting and Power Points, Home Theater Systems, TVS, Phones and Data
Im looking a business card, something nice, clean, modern and not to cluttered
Im open to sugestions
I dont mind if the "Services" is on the back on the business card
colours black, grey, white or the blue colour of my logo are prefered but not compulsory
any questions just message me
and please make it so if i need to edit the writing can do it easy. maybe by making it a seperate layer ?
My Details are.
Name - Peter Halloran
Job Title - Licenced Electrician
Mobile - 027 583 2174
Email - peter@kestrelelectrical.co.nz
Web - www.kestrelelectrical.co.nz
Services
Residential / Commercial
Lighting & Power
Heating & Ventilation
Automation
Phone & Data
Home Cinema
Sound Systems
TV, Antenna & Satellite
Digital Upgrades

```html
<!DOCTYPE html>
<html lang="en">
<head>
<meta charset="utf-8">
<title>Kestrel Electrical – Business Card</title>
<link href="https://fonts.googleapis.com/css2?family=Montserrat:wght@400;800&family=Tinos&family=Open+Sans:ital@1&display=swap" rel="stylesheet">
<style>
  :root {
    --brand-blue: #00a9c9;
    --ring-grey: #808184;
    --band-dark: #33322e;
    --ink-dark: #2f3033;
    --paper-light: #eceeef;
    --paper-mid: #d6d8da;
    --text-light: #ffffff;
  }
  * { margin: 0; padding: 0; box-sizing: border-box; }
  html, body {
    width: 967px; height: 1200px; overflow: hidden;
    background: #ffffff;
    font-family: "Montserrat", sans-serif;
  }
  .sheet { position: relative; width: 967px; height: 1200px; }
  .card {
    position: absolute; left: 51px; width: 901px; height: 521px;
    border-radius: 38px; overflow: hidden;
    background: linear-gradient(125deg, var(--paper-mid) 0%, var(--paper-light) 45%, #f6f7f7 58%, var(--paper-mid) 100%);
  }
  .card--front { top: 82px; }
  .card--back { top: 663px; }
  .card__band {
    position: absolute; left: 0; right: 0; top: 325px; bottom: 0;
    background: var(--band-dark);
  }
  .card__rings { position: absolute; inset: 0; width: 901px; height: 521px; }

  /* Wordmark */
  .wordmark {
    position: absolute; color: var(--brand-blue); font-weight: 800;
    text-transform: uppercase; line-height: 1; text-align: center;
  }
  .wordmark--large { left: 0; right: 0; top: 110px; font-size: 60px; letter-spacing: 3px; }
  .wordmark--large span { display: block; }
  .wordmark--large span + span { margin-top: 14px; }
  .wordmark--small { left: 60px; top: 46px; font-size: 20px; letter-spacing: 1px; text-align: left; }
  .wordmark--small span { display: block; }
  .wordmark--small span + span { margin-top: 4px; }

  /* Services */
  .services {
    position: absolute; top: 360px; left: 0; right: 0;
    color: var(--text-light); font-size: 19px; letter-spacing: 0.4px;
  }
  .services__col { position: absolute; width: 280px; list-style: none; text-align: center; }
  .services__col li { height: 35px; line-height: 35px; }
  .services__col--one { left: 123px; top: 5px; }
  .services__col--two { left: 365px; }
  .services__col--three { left: 597px; }

  /* Identity */
  .person {
    position: absolute; left: 0; right: 0; top: 160px; text-align: center; color: var(--ink-dark);
  }
  .person__name { font-family: "Tinos", serif; font-size: 76px; font-weight: 400; line-height: 1; }
  .person__title {
    font-family: "Open Sans", sans-serif; font-style: italic;
    font-size: 30px; letter-spacing: 1px; margin-top: 6px;
  }

  /* Contacts */
  .contacts {
    position: absolute; top: 362px; left: 0; right: 0; list-style: none;
    color: var(--text-light); font-size: 24px; letter-spacing: 0.3px;
  }
  .contacts__item {
    display: flex; align-items: center; justify-content: center;
    height: 36px; gap: 20px;
  }
  .contacts__icon { width: 30px; height: 24px; flex: none; }
</style>
</head>
<body>
<main class="sheet">

  <section class="card card--front" aria-label="Card front">
    <div class="card__band"></div>
    <svg class="card__rings" viewBox="0 0 901 521" aria-hidden="true">
      <ellipse cx="895" cy="181" rx="100" ry="94" fill="var(--brand-blue)"/>
      <ellipse cx="902" cy="181" rx="68" ry="61" fill="var(--ring-grey)"/>
      <ellipse cx="0" cy="381" rx="109" ry="93" fill="var(--brand-blue)"/>
      <ellipse cx="0" cy="381" rx="71" ry="61" fill="var(--ring-grey)"/>
    </svg>
    <h1 class="wordmark wordmark--large"><span>Kestrel</span><span>Electrical</span></h1>
    <div class="services">
      <ul class="services__col services__col--one">
        <li>Residential / Commercial</li>
        <li>Lighting &amp; Power</li>
        <li>Heating &amp; Ventilation</li>
      </ul>
      <ul class="services__col services__col--two">
        <li>Automation</li>
        <li>Phone &amp; Data</li>
        <li>Home Cinema</li>
      </ul>
      <ul class="services__col services__col--three">
        <li>Sound Systems</li>
        <li>TV, Antenna &amp; Satellite</li>
        <li>Digital Upgrades</li>
      </ul>
    </div>
  </section>

  <section class="card card--back" aria-label="Card back">
    <div class="card__band"></div>
    <svg class="card__rings" viewBox="0 0 901 521" aria-hidden="true">
      <ellipse cx="895" cy="181" rx="100" ry="94" fill="var(--brand-blue)"/>
      <ellipse cx="902" cy="181" rx="68" ry="61" fill="var(--ring-grey)"/>
      <ellipse cx="0" cy="381" rx="109" ry="93" fill="var(--brand-blue)"/>
      <ellipse cx="0" cy="381" rx="71" ry="61" fill="var(--ring-grey)"/>
    </svg>
    <p class="wordmark wordmark--small"><span>Kestrel</span><span>Electrical</span></p>
    <div class="person">
      <h2 class="person__name">Peter Halloran</h2>
      <p class="person__title">Licenced Electrician</p>
    </div>
    <ul class="contacts">
      <li class="contacts__item">
        <svg class="contacts__icon" viewBox="0 0 30 24" aria-hidden="true">
          <path d="M9 2c1.5 0 2.5 3.5 2.5 4.5S9.5 8.5 9.5 9.5c1 3 3 5 5.5 6 .8 0 2-2 3-2s4.5 1 4.5 2.5-1.5 4-3.5 4C11 20 4 13 4 5c0-2 3-3 5-3z" fill="var(--brand-blue)"/>
        </svg>
        <span>027 583 2174</span>
      </li>
      <li class="contacts__item">
        <svg class="contacts__icon" viewBox="0 0 30 24" aria-hidden="true">
          <rect x="2" y="4" width="26" height="17" fill="none" stroke="var(--brand-blue)" stroke-width="2"/>
          <path d="M2 4l13 10 13-10M2 21l10-8M28 21l-10-8" fill="none" stroke="var(--brand-blue)" stroke-width="2"/>
        </svg>
        <span>peter@kestrelelectrical.co.nz</span>
      </li>
      <li class="contacts__item">
        <svg class="contacts__icon" viewBox="0 0 30 24" aria-hidden="true">
          <g fill="none" stroke="var(--brand-blue)" stroke-width="1.6">
            <circle cx="15" cy="12" r="10.5"/>
            <ellipse cx="15" cy="12" rx="5" ry="10.5"/>
            <path d="M4.5 12h21M6 6.5h18M6 17.5h18M15 1.5v21"/>
          </g>
        </svg>
        <span>www.kestrelelectrical.co.nz</span>
      </li>
    </ul>
  </section>

</main>
</body>
</html>
```